Steadfast Valve Works

I need a business card with the attached logo.
The second page I have attached is what we are looking for. We want doubles sided. We would like the blues fading and the logo on the back.

Industry/Entity Type

Business

```html
<!DOCTYPE html>
<html lang="en">
<head>
<meta charset="utf-8">
<title>Steadfast Valve Works – Business Card</title>
<link href="https://fonts.googleapis.com/css2?family=Roboto:wght@400;500;700&display=swap" rel="stylesheet">
<style>
  :root {
    --page-bg: #e9e7e3;
    --card-black: #0d0d0f;
    --brand-blue: #2f6fd6;
    --navy: #1b2f6b;
    --deep-blue: #1c3f8f;
    --mid-blue: #2b5cc0;
    --white: #ffffff;
    --shadow: rgba(0, 0, 0, 0.28);
  }
  * { margin: 0; padding: 0; box-sizing: border-box; }
  html, body {
    width: 1200px;
    height: 902px;
    overflow: hidden;
    background: var(--page-bg);
    font-family: "Roboto", Arial, sans-serif;
  }
  .sheet {
    position: relative;
    width: 1200px;
    height: 902px;
  }
  .card {
    position: absolute;
    left: 280px;
    width: 640px;
    height: 366px;
    border-radius: 22px;
    overflow: hidden;
    box-shadow: 0 10px 28px var(--shadow);
  }
  /* Back side */
  .card--back {
    top: 40px;
    background: var(--card-black);
    display: flex;
    flex-direction: column;
    align-items: center;
    justify-content: center;
    gap: 30px;
  }
  .wordmark {
    font-weight: 700;
    text-transform: uppercase;
    letter-spacing: 2px;
    line-height: 1;
  }
  .card--back .wordmark {
    color: var(--brand-blue);
    font-size: 40px;
  }
  .back-url {
    color: var(--brand-blue);
    font-size: 15px;
    letter-spacing: 0.3px;
  }
  /* Front side */
  .card--front {
    top: 496px;
    background: linear-gradient(115deg,
      var(--deep-blue) 0%,
      var(--mid-blue) 42%,
      #6f8fd6 62%,
      #dfe6f6 80%,
      var(--white) 92%);
  }
  .card--front .wordmark {
    position: absolute;
    top: 58px;
    right: 42px;
    color: var(--navy);
    font-size: 26px;
  }
  .holder {
    position: absolute;
    left: 48px;
    top: 170px;
    color: var(--white);
  }
  .holder-name {
    font-size: 24px;
    font-weight: 500;
  }
  .holder-role {
    font-size: 14px;
    margin-top: 4px;
    opacity: 0.92;
  }
  .contact-list {
    position: absolute;
    left: 200px;
    top: 238px;
    list-style: none;
    color: var(--white);
    font-size: 13px;
  }
  .contact-item {
    display: flex;
    align-items: flex-start;
    gap: 10px;
    margin-bottom: 7px;
    line-height: 1.4;
  }
  .contact-icon {
    width: 12px;
    height: 12px;
    margin-top: 3px;
    flex-shrink: 0;
    fill: var(--white);
  }
</style>
</head>
<body>
<main class="sheet">

  <section class="card card--back" aria-label="Card back">
    <div class="wordmark">Steadfast Valve Works</div>
    <div class="back-url">www.steadfastvalveworks.com</div>
  </section>

  <section class="card card--front" aria-label="Card front">
    <div class="wordmark">Steadfast Valve Works</div>

    <div class="holder">
      <div class="holder-name">Dalton Pierce</div>
      <div class="holder-role">Business Development Manager</div>
    </div>

    <ul class="contact-list">
      <li class="contact-item">
        <svg class="contact-icon" viewBox="0 0 12 12"><path d="M6 0a4 4 0 0 0-4 4c0 3 4 8 4 8s4-5 4-8a4 4 0 0 0-4-4zm0 5.6A1.6 1.6 0 1 1 6 2.4a1.6 1.6 0 0 1 0 3.2z"/></svg>
        <span>820 Ridgeline Avenue<br>Marlow, GA 30999</span>
      </li>
      <li class="contact-item">
        <svg class="contact-icon" viewBox="0 0 12 12"><path d="M2.4 0.6l1.8 0 0.9 2.6-1.3 1a7 7 0 0 0 3 3l1-1.3 2.6 0.9v1.8a1.2 1.2 0 0 1-1.3 1.2A10 10 0 0 1 1.2 1.9 1.2 1.2 0 0 1 2.4 0.6z"/></svg>
        <span>404 555 0192</span>
      </li>
      <li class="contact-item">
        <svg class="contact-icon" viewBox="0 0 12 12"><path d="M0 2h12v8H0z M0.8 2.6 6 6.6l5.2-4" fill="none" stroke="#fff" stroke-width="1.2"/></svg>
        <span>steadfastvalve@mail.com</span>
      </li>
      <li class="contact-item">
        <svg class="contact-icon" viewBox="0 0 12 12"><circle cx="6" cy="6" r="5.3" fill="none" stroke="#fff" stroke-width="1.1"/><path d="M0.7 6h10.6M6 0.7c-3 3-3 7.6 0 10.6M6 0.7c3 3 3 7.6 0 10.6" fill="none" stroke="#fff" stroke-width="1"/></svg>
        <span>www.steadfastvalveworks.com</span>
      </li>
    </ul>
  </section>

</main>
</body>
</html>
```